Copper wren builds

Copper wren builds is a small construction company.
Who is a licenced builder, Carpenter, joiner,
working on heritage ,new build, speacial projects and sometimes furniture

Industry/Entity Type

Construction

```html
<!DOCTYPE html>
<html lang="en">
<head>
<meta charset="utf-8">
<title>Copper wren builds – Business Card</title>
<link rel="stylesheet" href="https://fonts.googleapis.com/css2?family=Roboto+Slab:wght@400;500&family=Open+Sans:wght@400;600&display=swap">
<style>
  :root {
    --backdrop: #e6e4e1;
    --card-white: #fbfbfa;
    --card-black: #141414;
    --brand-green: #23a31f;
    --ink-dark: #3b3b3b;
    --ink-mid: #5a5a5a;
    --rule: #9a9a9a;
  }
  * { box-sizing: border-box; margin: 0; padding: 0; }
  html, body {
    width: 1200px;
    height: 844px;
    overflow: hidden;
    background: var(--backdrop);
  }
  .canvas {
    position: relative;
    width: 1200px;
    height: 844px;
  }
  .card {
    position: absolute;
    top: 272px;
    width: 520px;
    height: 300px;
    border-radius: 3px;
    box-shadow: 0 6px 18px rgba(0,0,0,0.18);
  }
  .card-front {
    left: 50px;
    background: var(--card-white);
    font-family: "Open Sans", Arial, sans-serif;
    color: var(--ink-mid);
  }
  .card-back {
    left: 630px;
    background: var(--card-black);
  }
  .brand {
    position: absolute;
    right: 34px;
    top: 34px;
    display: flex;
    align-items: center;
    gap: 10px;
  }
  .brand-dot {
    width: 16px;
    height: 16px;
    border-radius: 50%;
    background: var(--brand-green);
  }
  .brand-name {
    font-family: "Roboto Slab", Georgia, serif;
    font-size: 19px;
    font-weight: 400;
    color: var(--ink-dark);
  }
  .rule {
    position: absolute;
    left: 34px;
    right: 34px;
    height: 1px;
    background: var(--rule);
  }
  .rule-top { top: 96px; }
  .rule-mid { top: 212px; }
  .holder {
    position: absolute;
    left: 34px;
    top: 120px;
  }
  .holder-name {
    font-family: "Roboto Slab", Georgia, serif;
    font-size: 22px;
    font-weight: 400;
    color: var(--ink-dark);
    line-height: 1.1;
  }
  .holder-name .first { color: var(--brand-green); }
  .holder-role {
    font-size: 12px;
    margin-top: 3px;
  }
  .address {
    position: absolute;
    left: 34px;
    top: 180px;
    font-size: 12px;
  }
  .contacts {
    position: absolute;
    left: 34px;
    top: 226px;
    font-size: 12px;
    line-height: 1.7;
    color: var(--ink-mid);
  }
  .contacts .label { color: var(--brand-green); }
  .contacts .web { color: var(--brand-green); margin-left: 8px; }
  .contacts .sep { margin-left: 8px; }
  .back-brand {
    position: absolute;
    right: 40px;
    top: 118px;
    display: flex;
    align-items: center;
    gap: 10px;
  }
  .back-brand .brand-name { color: #e6e6e6; font-size: 18px; }
</style>
</head>
<body>
<main class="canvas">
  <section class="card card-front" aria-label="Business card front">
    <div class="brand">
      <span class="brand-dot"></span>
      <span class="brand-name">Copper wren builds</span>
    </div>
    <div class="rule rule-top"></div>
    <div class="holder">
      <p class="holder-name"><span class="first">Marlow</span> Hayes</p>
      <p class="holder-role">Managing Director</p>
    </div>
    <p class="address">12345, Address Goes Here Country Name, 123456.</p>
    <div class="rule rule-mid"></div>
    <div class="contacts">
      <p><span class="label">T:</span>(044) 123 456 789<span class="sep"><span class="label">F:</span>(044) 123456789</span><span class="sep"><span class="label">M:</span>(044)123456789</span></p>
      <p><span class="label">E:</span>info@youremail.com<span class="web">www.yourweb.com</span></p>
    </div>
  </section>

  <section class="card card-back" aria-label="Business card back">
    <div class="back-brand">
      <span class="brand-dot"></span>
      <span class="brand-name">Copper wren builds</span>
    </div>
  </section>
</main>
</body>
</html>
```